Letterhead and compliment slip

We are a UK-based market research agency. We are looking for a new letterhead design to incorporate our logo, address details and company information. We are looking for a simple design. It should be modern. It needs to have a qualify feel. As we are UK based it needs to be designed for A4 paper size (letterhead).
I'm really looking for something simple in design terms!
Both letterhead and compliment slip need to include:
Our logo
Company address
Telephone number
Email address
Website address
Company registration number
VAT registration number
Grey and green would be a good colour scheme to fit with our logo

```html
<!DOCTYPE html>
<html lang="en">
<head>
<meta charset="utf-8">
<title>Brightline Research – Letterhead and Compliment Slip</title>
<link rel="stylesheet" href="https://fonts.googleapis.com/css2?family=Fira+Sans:wght@400;500;600&display=swap">
<style>
  :root {
    --green: #a8cb3a;
    --green-light: #cadd3e;
    --ink: #2f2f2f;
    --backdrop: #e6e6e6;
    --paper: #ffffff;
  }
  * { box-sizing: border-box; margin: 0; padding: 0; }
  html, body { width: 1200px; height: 1200px; overflow: hidden; }
  body {
    background: var(--backdrop);
    font-family: "Fira Sans", Arial, sans-serif;
    color: var(--ink);
    position: relative;
  }

  /* Letterhead */
  .letterhead {
    position: absolute; left: 56px; top: 94px;
    width: 718px; height: 1015px;
    background: var(--paper);
  }
  .letterhead__brand {
    position: absolute; left: 1px; top: 22px;
    width: 246px; height: 82px;
    background: var(--green);
    display: flex; align-items: center; justify-content: center;
  }
  .brand-name {
    font-weight: 600; font-size: 30px; letter-spacing: -0.3px;
  }
  .letterhead__brand .brand-name { color: #fff; }
  .letterhead__web {
    position: absolute; left: 29px; top: 118px;
    font-size: 11px; letter-spacing: 1.6px;
  }
  .letterhead__address {
    position: absolute; left: 277px; top: 42px;
    font-size: 10.5px; line-height: 18px;
  }
  .letterhead__divider {
    position: absolute; left: 506px; top: 30px;
    width: 1px; height: 68px; background: var(--green);
  }
  .letterhead__contact {
    position: absolute; left: 537px; top: 48px;
    font-size: 10.5px; line-height: 18px;
  }
  .letterhead__footer {
    position: absolute; left: 0; top: 950px;
    width: 100%; height: 41px;
    background: var(--green);
    display: flex; align-items: center; justify-content: center;
    font-size: 10.5px; color: var(--ink);
  }
  .sep { margin: 0 9px; }

  /* Compliment slip */
  .slip {
    position: absolute; left: 812px; top: 392px;
    width: 338px; height: 718px;
    background: var(--paper);
    overflow: hidden;
  }
  .slip__face {
    position: absolute; left: 338px; top: 0;
    width: 718px; height: 338px;
    transform-origin: 0 0;
    transform: rotate(90deg);
  }
  .slip__pattern { position: absolute; left: 0; top: 0; }
  .slip__brand {
    position: absolute; left: 30px; top: 190px;
  }
  .slip__brand .brand-name { color: var(--green); font-size: 34px; }
  .slip__address {
    position: absolute; left: 30px; top: 254px;
    font-size: 10px; line-height: 17.5px;
  }
  .slip__contact {
    position: absolute; left: 30px; top: 298px;
    font-size: 10px;
  }
  .slip__rule-short {
    position: absolute; left: 316px; top: 309px;
    width: 146px; height: 1px; background: var(--green);
  }
  .slip__web {
    position: absolute; left: 474px; top: 301px;
    font-size: 11px; letter-spacing: 1.6px;
  }
  .slip__rule-long {
    position: absolute; left: 252px; top: 18px;
    width: 444px; height: 1px; background: var(--green);
  }
</style>
</head>
<body>

<section class="letterhead" aria-label="A4 letterhead">
  <div class="letterhead__brand"><span class="brand-name">Brightline</span></div>
  <p class="letterhead__web">www.brightlineresearch.co.uk</p>
  <address class="letterhead__address" style="font-style:normal">
    Brightline Research Ltd.<br>
    12 Willow Yard&nbsp; | &nbsp;Mill Lane | Eastfield<br>
    Ashford |&nbsp; Kent&nbsp; | &nbsp;TN24 8QR
  </address>
  <div class="letterhead__divider"></div>
  <p class="letterhead__contact">
    +44 (0)1632 960418<br>
    hello@brightlineresearch.co.uk
  </p>
  <footer class="letterhead__footer">
    Company Registration Number : 6184027<span class="sep">|</span>VAT Registration Number : 731620458
  </footer>
</section>

<section class="slip" aria-label="Compliment slip">
  <div class="slip__face">
    <svg class="slip__pattern" width="270" height="172" viewBox="0 0 270 172" role="img" aria-label="Cluster of lime green triangles as a corner decoration">
      <defs>
        <linearGradient id="slipGlow" x1="0" y1="0" x2="1" y2="1">
          <stop offset="0" stop-color="#cadd3e"/>
          <stop offset="1" stop-color="#a5c83a"/>
        </linearGradient>
      </defs>
      <polygon points="8,0 268,0 210,62 150,112 80,150 50,125 20,90 0,40" fill="url(#slipGlow)"/>
    </svg>
    <div class="slip__brand"><span class="brand-name">Brightline</span></div>
    <p class="slip__address">
      Brightline Research Ltd. | 12 Willow Yard | Mill Lane<br>
      Eastfield | Ashford | Kent | TN24 8QR
    </p>
    <p class="slip__contact">hello@brightlineresearch.co.uk | +44 (0)1632 960418</p>
    <div class="slip__rule-short"></div>
    <p class="slip__web">www.brightlineresearch.co.uk</p>
    <div class="slip__rule-long"></div>
  </div>
</section>

</body>
</html>
```